Flyer for Custom Home Builder!

my company is Harlow Ridge Homes, I am looking for a flyer that we can send via email to a customer, or print and hand out. I am thinking four pages so we could print this and fold it., possibly creating a folder. The name of the company is Harlow Ridge Homes our website is here www.harlowridgehomes-example.com. Some text you can use "Crafting luxury homes isn't just a job, it's our passion.
With meticulous attention to detail and an unwavering commitment to using the finest materials, Harlow Ridge Homes consistently delivers exceptional results that stand as a testament to our commitment to quality."

"Trust is the cornerstone of our foundation.
With a proven track record of delivering on our promises for over 16 years, we prioritize transparent communication and integrity throughout every step of the home-building journey".

you may need to obtain the photos here
https://files.example-share.net/f/k27pw4m8zrt03xq61bnv/h?key=48vn2c9q1x7mb5t0ekd3h&dl=0

Target Market(s)

We build homes for every wealthy clients, therefore the photos are extremely important

Industry/Entity Type

Construction.

Requirements
Must have
• clear larger photos

```html
<!DOCTYPE html>
<html lang="en">
<head>
<meta charset="utf-8">
<title>Harlow Ridge Homes – Flyer Cover</title>
<link href="https://fonts.googleapis.com/css2?family=Bebas+Neue&family=Montserrat:wght@700;800&family=Open+Sans:ital,wght@0,300;0,400;0,700;1,400&display=swap" rel="stylesheet">
<style>
  :root{
    --tan:#e9c39b;
    --brown:#b8987c;
    --charcoal:#3d3d3d;
    --black:#0b0a0a;
    --white:#ffffff;
    --logo-grey:#3a3a3a;
  }
  *{margin:0;padding:0;box-sizing:border-box;}
  html,body{width:851px;height:1200px;overflow:hidden;background:var(--white);}
  .flyer{position:relative;width:851px;height:1200px;overflow:hidden;background:var(--white);}

  .hero-art{position:absolute;left:0;top:0;width:851px;height:800px;}

  .band{position:absolute;left:0;width:851px;}
  .band.right{left:485px;width:366px;}
  .tan{background:var(--tan);}
  .brown{background:var(--brown);}
  .charcoal{background:var(--charcoal);}
  .black{background:var(--black);}

  .brand{
    position:absolute;left:506px;top:62px;width:320px;
    font-family:"Montserrat",sans-serif;font-weight:800;
    color:var(--logo-grey);text-transform:uppercase;
    font-size:31px;line-height:36px;letter-spacing:1px;text-align:center;
  }

  .headline{
    position:absolute;left:498px;top:302px;width:345px;
    font-family:"Bebas Neue",sans-serif;font-weight:400;font-size:52px;line-height:49.5px;
    letter-spacing:.3px;color:var(--white);text-transform:uppercase;
  }
  .headline .dark{color:var(--charcoal);}

  .feature{
    position:absolute;top:822px;width:244px;height:228px;border-radius:50%;
    overflow:hidden;box-shadow:4px 4px 6px rgba(0,0,0,.45);
    color:var(--white);text-align:center;
  }
  .feature .photo{position:absolute;inset:0;}
  .feature .num{
    position:absolute;left:0;right:0;top:16px;
    font-family:"Montserrat",sans-serif;font-weight:700;font-size:100px;line-height:100px;
    color:var(--tan);letter-spacing:-3px;text-shadow:1px 2px 3px rgba(0,0,0,.35);
  }
  .feature .title{
    position:absolute;left:0;right:0;top:122px;
    font-family:"Open Sans",sans-serif;font-size:23px;line-height:28px;font-weight:300;
  }
  .feature .title b{font-weight:700;}
  .feature .desc{
    position:absolute;left:42px;right:42px;top:157px;
    font-family:"Open Sans",sans-serif;font-size:15.5px;line-height:19px;
    text-align:justify;text-align-last:justify;
  }

  .closing{
    position:absolute;left:30px;right:30px;top:1097px;
    font-family:"Open Sans",sans-serif;font-style:italic;font-size:18.5px;line-height:26px;
    letter-spacing:1.2px;color:var(--charcoal);text-align:center;
  }
</style>
</head>
<body>
<main class="flyer">

  <svg class="hero-art" viewBox="0 0 851 800">
    <defs>
      <linearGradient id="bathTone" x1="0" y1="0" x2="1" y2="1">
        <stop offset="0" stop-color="#ebe9e7"/>
        <stop offset=".55" stop-color="#dcd8d3"/>
        <stop offset="1" stop-color="#cfc7bc"/>
      </linearGradient>
    </defs>
    <rect class="frame-shadow" x="85" y="95" width="400" height="690" rx="70" fill="#3d3d3d"/>
    <path role="img" aria-label="Bathroom interior with a wooden vanity and a dark open shelf holding rolled towels and baskets"
          d="M0,0 H450 V695 A60,60 0 0 1 390,755 H0 Z" fill="url(#bathTone)"/>
  </svg>

  <div class="brand">Harlow Ridge<br>Homes</div>

  <div class="band right tan" style="top:219px;height:16px;"></div>
  <div class="band right tan" style="top:260px;height:15px;"></div>
  <div class="band right brown" style="top:275px;height:16px;"></div>
  <div class="band right tan" style="top:291px;height:320px;"></div>
  <div class="band right tan" style="top:637px;height:13px;"></div>
  <div class="band right brown" style="top:650px;height:17px;"></div>
  <div class="band right tan" style="top:667px;height:21px;"></div>

  <h1 class="headline">
    Crafting luxury<br>homes isn't<br>
    <span class="dark">just a job,<br>it's our passion.</span><br>
    Trust is the<br>cornerstone
  </h1>

  <div class="band charcoal" style="top:867px;height:12px;"></div>
  <div class="band tan" style="top:893px;height:134px;"></div>
  <div class="band black" style="top:1027px;height:40px;"></div>
  <div class="band tan" style="top:1067px;height:118px;"></div>
  <div class="band brown" style="top:1185px;height:15px;"></div>

  <section class="feature" style="left:55px;">
    <div class="photo" role="img" aria-label="Stone-clad luxury home exterior at dusk" style="background:linear-gradient(160deg,#8f949b 0%,#6e7176 50%,#55595a 100%);"></div>
    <div class="num">01</div>
    <div class="title">Fine<b>Materials</b></div>
    <p class="desc">Built with the finest materials</p>
  </section>

  <section class="feature" style="left:303px;">
    <div class="photo" role="img" aria-label="Modern two-storey home with large lit windows at dusk" style="background:linear-gradient(160deg,#9a9ea5 0%,#6f747b 50%,#4d5155 100%);"></div>
    <div class="num">02</div>
    <div class="title">Proven<b>Trust</b></div>
    <p class="desc">Promises kept for over 16 years</p>
  </section>

  <section class="feature" style="left:551px;">
    <div class="photo" role="img" aria-label="Backyard pool terrace of a luxury home at dusk" style="background:linear-gradient(160deg,#8c9098 0%,#6a6c70 50%,#4f4f4c 100%);"></div>
    <div class="num">03</div>
    <div class="title">Open<b>Dialogue</b></div>
    <p class="desc">Transparent talk at every step</p>
  </section>

  <p class="closing">Transparent communication and integrity at every step.<br>www.harlowridgehomes-example.com</p>

</main>
</body>
</html>
```